Trade Show Flyer

Business card sized Bi-fold handout with Logo, description of services on inside and contact info on the back. Could use artwork/photos as watermark background or strategically locate without cluttering.

Target Market(s)

Contractors in the deep foundation industry

Industry/Entity Type

Construction

Colors

Designer to choose colors to be used in the design.

Requirements
Must have
• Cool use of Logo, artwork and photos, description of various services, contact info
Nice to have
• Logo of Terravox and BK&R incorporated
Should not have
• too busy

```html
<!DOCTYPE html>
<html lang="en">
<head>
<meta charset="utf-8">
<title>DeepBore Supply – Trade Show Handout</title>
<link href="https://fonts.googleapis.com/css2?family=Open+Sans:wght@400;600;700&display=swap" rel="stylesheet">
<style>
:root{
  --bg:#3a3a3c;
  --charcoal:#2e2e30;
  --yellow:#f5c400;
  --blue:#1e63b8;
  --paper:#ffffff;
  --paper-cool:#eef1f5;
  --ink:#333;
  --ink-soft:#555;
}
*{margin:0;padding:0;box-sizing:border-box}
html,body{width:1200px;height:1000px;overflow:hidden;background:var(--bg);font-family:"Open Sans",sans-serif;color:var(--ink)}
.spread{position:absolute;left:50px;width:1100px;height:470px;overflow:hidden;background:var(--paper)}
.spread--outside{top:20px}
.spread--inside{top:510px;background:var(--paper-cool)}
.spread svg.art{position:absolute;left:0;top:0}
.fold{position:absolute;top:0;left:549px;width:2px;height:470px;background:rgba(0,0,0,.08)}
.brand{position:absolute;display:flex;align-items:center;gap:8px;font-weight:700;color:var(--blue);font-size:20px;letter-spacing:.5px;white-space:nowrap}
.brand-mark{width:18px;height:18px;background:var(--blue)}
.contact{position:absolute;font-size:13px;line-height:1.45;color:var(--ink)}
.contact-name{font-weight:600;font-size:14px}
.contact-row{display:flex;align-items:center;gap:6px}
.contact-row svg{flex:none}
.url-bar{position:absolute;font-weight:600;letter-spacing:3px;font-size:14px}
.url-bar--back{left:0;top:430px;width:550px;text-align:center;line-height:40px;color:var(--charcoal)}
.url-bar--inside{top:440px;width:550px;text-align:center;line-height:30px;color:#fff;font-size:13px}
.intro{position:absolute;left:40px;top:130px;width:480px}
.intro h2{font-size:19px;font-weight:600;color:var(--charcoal);margin-bottom:3px;line-height:1.3}
.intro p{font-size:9px;line-height:12px;color:var(--ink-soft)}
.intro strong{color:var(--charcoal)}
.gallery{position:absolute;left:40px;top:250px;display:grid;grid-template-columns:repeat(3,150px);grid-auto-rows:66px;gap:8px}
.gallery .photo{display:block}
.partners{position:absolute;left:190px;top:398px;display:flex;align-items:center;gap:12px}
.partner-badge{width:40px;height:22px;border-radius:50%;background:var(--blue)}
.partner-divider{width:1px;height:24px;background:#999}
.partner-name{font-size:16px;font-weight:700;color:var(--blue)}
.services-title{position:absolute;left:550px;width:550px;top:86px;text-align:center;font-size:20px;font-weight:600;color:var(--charcoal)}
.service{position:absolute;left:595px;width:440px;height:92px;border:2px dashed var(--blue);border-radius:10px;background:rgba(255,255,255,.55);padding:8px 40px}
.service-head{display:flex;align-items:center;justify-content:center;gap:10px;margin-bottom:4px}
.service-brand{display:flex;align-items:center;gap:5px;font-weight:700;color:var(--blue);font-size:13px}
.service-brand i{display:block;width:11px;height:11px;background:var(--blue)}
.service-title{font-size:12px;font-weight:700;color:var(--blue);line-height:1.15;text-transform:uppercase}
.service p{font-size:10px;line-height:13px;color:var(--ink-soft);text-align:center}
.quote{position:absolute;font-size:30px;font-weight:700;color:var(--blue);line-height:1}
.quote--open{left:10px;top:4px}
.quote--close{right:10px;bottom:-8px}
</style>
</head>
<body>

<section class="spread spread--outside">
  <svg class="art" width="1100" height="470" viewBox="0 0 1100 470">
    <defs>
      <linearGradient id="siteTone" x1="0" y1="0" x2="0" y2="1">
        <stop offset="0" stop-color="#5b7fb4"/>
        <stop offset=".55" stop-color="#8a7a5e"/>
        <stop offset="1" stop-color="#6e5a3e"/>
      </linearGradient>
      <linearGradient id="rigTone" x1="0" y1="0" x2="1" y2="1">
        <stop offset="0" stop-color="#4f86d1"/>
        <stop offset=".5" stop-color="#c9c3b6"/>
        <stop offset=".85" stop-color="#9a7b55"/>
        <stop offset="1" stop-color="#e08a10"/>
      </linearGradient>
    </defs>
    <rect x="0" y="0" width="550" height="300" fill="var(--charcoal)"/>
    <path role="img" aria-label="Photo of a deep foundation job site with crawler cranes and drill rigs" d="M0,95 L330,18 L550,250 L550,300 Q275,255 0,292 Z" fill="url(#siteTone)"/>
    <polyline points="0,84 330,6 550,236" fill="none" stroke="var(--yellow)" stroke-width="10"/>
    <path d="M0,292 Q275,255 550,300 L550,470 L0,470 Z" fill="var(--paper)"/>
    <path d="M0,292 Q275,255 550,300" fill="none" stroke="var(--yellow)" stroke-width="7"/>
    <rect x="0" y="430" width="550" height="40" fill="var(--yellow)"/>
    <rect x="0" y="424" width="550" height="3" fill="#d9d9d9"/>
    <rect x="550" y="0" width="550" height="470" fill="var(--charcoal)"/>
    <path role="img" aria-label="Photo of a white and blue hydraulic drill rig working on a dirt site" d="M835,62 L1100,195 L1100,470 L655,470 Z" fill="url(#rigTone)"/>
    <polygon points="765,28 805,42 625,470 585,470" fill="#e4e6ea"/>
    <polygon points="805,42 838,58 658,470 625,470" fill="var(--yellow)"/>
    <polyline points="836,60 1100,192" fill="none" stroke="var(--yellow)" stroke-width="9"/>
  </svg>
  <div class="fold"></div>

  <div class="brand" style="left:150px;top:322px">
    <span class="brand-mark"></span>DeepBore Supply
  </div>

  <div class="contact" style="left:60px;top:365px">
    <div class="contact-name">Glen Harlow</div>
    <div class="contact-row"><svg width="11" height="11" viewBox="0 0 24 24"><path d="M6.6 10.8a15 15 0 0 0 6.6 6.6l2.2-2.2c.3-.3.7-.4 1-.2 1.1.4 2.3.6 3.6.6.6 0 1 .4 1 1V20c0 .6-.4 1-1 1A17 17 0 0 1 3 4c0-.6.4-1 1-1h3.5c.6 0 1 .4 1 1 0 1.3.2 2.5.6 3.6.1.3 0 .7-.2 1z" fill="#333"/></svg>555-201-4418</div>
    <div class="contact-row"><svg width="11" height="11" viewBox="0 0 24 24"><path d="M2 5h20v14H2z" fill="#333"/><path d="M2 5l10 8 10-8" fill="none" stroke="#fff" stroke-width="2"/></svg>gharlow@deepboresupply.com</div>
  </div>

  <div class="contact" style="left:310px;top:365px">
    <div class="contact-name">TJ Vandermeer</div>
    <div class="contact-row"><svg width="11" height="11" viewBox="0 0 24 24"><path d="M6.6 10.8a15 15 0 0 0 6.6 6.6l2.2-2.2c.3-.3.7-.4 1-.2 1.1.4 2.3.6 3.6.6.6 0 1 .4 1 1V20c0 .6-.4 1-1 1A17 17 0 0 1 3 4c0-.6.4-1 1-1h3.5c.6 0 1 .4 1 1 0 1.3.2 2.5.6 3.6.1.3 0 .7-.2 1z" fill="#333"/></svg>(555) 933-0172</div>
    <div class="contact-row"><svg width="11" height="11" viewBox="0 0 24 24"><path d="M2 5h20v14H2z" fill="#333"/><path d="M2 5l10 8 10-8" fill="none" stroke="#fff" stroke-width="2"/></svg>tj@deepboresupply.com</div>
  </div>

  <div class="url-bar url-bar--back">www.deepboresupply.com</div>

  <div class="brand" style="left:565px;top:34px;font-size:17px">
    <span class="brand-mark"></span>DeepBore Supply
  </div>
</section>

<section class="spread spread--inside">
  <svg class="art" width="1100" height="470" viewBox="0 0 1100 470">
    <defs>
      <linearGradient id="hazeTone" x1="0" y1="0" x2="1" y2="1">
        <stop offset="0" stop-color="#eef1f5"/>
        <stop offset=".6" stop-color="#dde3ea"/>
        <stop offset="1" stop-color="#e9ecf0"/>
      </linearGradient>
    </defs>
    <rect role="img" aria-label="Faint background photo of a drill rig" x="550" y="0" width="550" height="470" fill="url(#hazeTone)"/>
    <path d="M0,0 H550 V95 L340,16 L0,66 Z" fill="var(--charcoal)"/>
    <polyline points="0,74 340,24 550,104" fill="none" stroke="var(--yellow)" stroke-width="8"/>
    <path d="M550,0 H1100 V90 L880,14 L550,78 Z" fill="var(--charcoal)"/>
    <polyline points="550,86 880,22 1100,98" fill="none" stroke="var(--yellow)" stroke-width="8"/>
    <polygon points="0,430 550,415 1100,430 1100,440 0,440" fill="#c9ccd1"/>
    <rect x="0" y="440" width="1100" height="30" fill="var(--charcoal)"/>
  </svg>
  <div class="fold"></div>

  <div class="brand" style="left:170px;top:98px;font-size:18px">
    <span class="brand-mark"></span>DeepBore Supply
  </div>

  <div class="intro">
    <h2>Introduction</h2>
    <p>We give contractors a place to list equipment with no upfront fees and free marketing until sold, reaching thousands of buyers in the foundation drilling trade worldwide. High demand for good used equipment means your listing gets seen fast. We specialize in used foundation drill rigs and work with <strong>TERRAVOX, KRANER, BAYLINE, LODEX, TESCOR, TEXRIG, IMTEC, SPIRALON, WALDEN, BERROW, CASARO, ABCO, HUTTON</strong> and <strong>TEVAR</strong> just to mention a few.</p>
  </div>

  <div class="gallery">
    <svg class="photo" width="150" height="66" role="img" aria-label="Photo of a blue drill rig on a hillside"><rect width="150" height="66" fill="#4d78ad"/></svg>
    <svg class="photo" width="150" height="66" role="img" aria-label="Photo of a drill rig mast against a pale sky"><rect width="150" height="66" fill="#9ea7ad"/></svg>
    <svg class="photo" width="150" height="66" role="img" aria-label="Photo of a blue and white rig cab close up"><rect width="150" height="66" fill="#2f6fc4"/></svg>
    <svg class="photo" width="150" height="66" role="img" aria-label="Photo of a rig lifting a soil-filled auger"><rect width="150" height="66" fill="#8f8a7c"/></svg>
    <svg class="photo" width="150" height="66" role="img" aria-label="Photo of a drilling tool silhouetted at sunset"><rect width="150" height="66" fill="#6b4a2c"/></svg>
    <svg class="photo" width="150" height="66" role="img" aria-label="Photo of rigs and tools in an equipment yard"><rect width="150" height="66" fill="#7d8fa3"/></svg>
  </div>

  <div class="partners">
    <span class="partner-badge"></span>
    <span class="partner-divider"></span>
    <span class="partner-name">Terravox</span>
  </div>

  <div class="url-bar url-bar--inside" style="left:0">www.deepboresupply.com</div>
  <div class="url-bar url-bar--inside" style="left:550px">www.deepboresupply.com</div>

  <h2 class="services-title">OUR SERVICES</h2>

  <article class="service" style="top:122px">
    <span class="quote quote--open">“</span>
    <div class="service-head">
      <span class="service-brand"><i></i>DeepBore</span>
      <span class="service-title">Rentals</span>
    </div>
    <p>Now offering a complete line of foundation drilling tools, support equipment and drill rigs for RENT. Find out more or call 555-201-4418.</p>
    <span class="quote quote--close">”</span>
  </article>

  <article class="service" style="top:220px">
    <span class="quote quote--open">“</span>
    <div class="service-head">
      <span class="service-brand"><i></i>DeepBore</span>
      <span class="service-title">New Terravox rigs<br>available immediately</span>
    </div>
    <p>New Terravox hydraulic drill rigs in stock in Texas, Rhode Island, California, New York and Utah, ready for delivery in North America.</p>
    <span class="quote quote--close">”</span>
  </article>

  <article class="service" style="top:318px">
    <span class="quote quote--open">“</span>
    <div class="service-head">
      <span class="service-brand"><i></i>DeepBore</span>
      <span class="service-title">Sell your<br>foundation drill rig</span>
    </div>
    <p>Drill rigs for sale including Terravox, Kraner, Bayline, Lodex, Tescor, Texrig, Imtec, Spiralon, Walden, Berrow, Casaro, Abco, Hutton, Tevar.</p>
    <span class="quote quote--close">”</span>
  </article>
</section>

</body>
</html>
```